Ned Halvorsen Executive Coach Business Card Design

I need a new card design for my Executive Coaching practice. I am a Clinical Psychotherapist and Executive Coach. I help my clients get the most out of life by developing their personal and professional skills and abilities.

I work with senior executives. My design needs to be high end. I am thinking gloss on the front. I am also thinking contemporary. I am going to use a black, grey and red colour scheme on the the website. I am thinking grey with black and red accents. I would also like a water mark included on the card.

Target Market(s)

Senior Executives In major Companies

Industry/Entity Type

Business

Contact Information for Business Card

On the front

Ned Halvorsen
Clinical Psychotherapist and Executive Coach
For Personal and Professional Success

On the Back

Tarrant office
87 Tarrant Vale Road Tarrant

North Sydney Office
Suite 309 / 41 Pellow Street North Sydney

Danforth Street Office
Suite 512 / 248 Danforth Street Sydney CBD

Phone 02 95517384
Email ned@nedhalvorsen.example.au

Requirements
Must have
• Friendly but professional
Water Mark
Gloss Front

```html
<!DOCTYPE html>
<html lang="en">
<head>
<meta charset="utf-8">
<title>Ned Halvorsen – Business Card</title>
<link rel="stylesheet" href="https://fonts.googleapis.com/css2?family=Bitter:wght@400;600&display=swap">
<style>
  :root {
    --backdrop: #d9d9d9;
    --card-black: #050505;
    --card-white: #ffffff;
    --ink: #1d1d1d;
    --ink-soft: #2b2b2b;
    --divider: #c9c9c9;
    --accent-red: #e3170a;
    --accent-black: #111111;
  }
  * { box-sizing: border-box; margin: 0; padding: 0; }
  html, body {
    width: 1200px; height: 492px; overflow: hidden;
    background: var(--backdrop);
    font-family: "Bitter", Georgia, serif;
  }
  .stage { position: relative; width: 1200px; height: 492px; }

  .card {
    position: absolute; top: 91px;
    width: 540px; height: 310px;
    box-shadow: 0 6px 18px rgba(0,0,0,.25);
    overflow: hidden;
  }

  /* Front */
  .card-front {
    left: 40px;
    background: var(--card-black);
    color: #fff;
    display: flex; flex-direction: column; align-items: center; justify-content: center;
    text-align: center;
  }
  .front-name { font-size: 44px; font-weight: 400; letter-spacing: .5px; margin-bottom: 12px; }
  .front-tagline { font-size: 19px; line-height: 1.3; }

  /* Back */
  .card-back { left: 620px; background: var(--card-white); color: var(--ink); }
  .addresses {
    position: absolute; top: 58px; right: 294px;
    display: flex; flex-direction: column; gap: 20px;
    text-align: right; font-size: 13px; line-height: 1.3;
    white-space: nowrap;
  }
  .address { display: flex; align-items: flex-start; gap: 7px; justify-content: flex-end; }
  .address .icon { margin-top: 2px; }
  .divider {
    position: absolute; top: 40px; left: 260px;
    width: 1px; height: 140px; background: var(--divider);
  }
  .contact {
    position: absolute; top: 42px; left: 274px; right: 12px;
    font-size: 14px; color: var(--ink-soft);
    white-space: nowrap;
  }
  .contact-name { font-size: 17px; font-weight: 600; color: var(--ink); margin-bottom: 30px; }
  .contact-list { list-style: none; display: flex; flex-direction: column; gap: 5px; }
  .contact-list li { display: flex; align-items: center; gap: 5px; }
  .icon { width: 12px; height: 12px; flex: none; fill: var(--ink); }
  .bands { position: absolute; left: 0; bottom: 0; width: 540px; height: 60px; }
</style>
</head>
<body>
<main class="stage">
  <section class="card card-front" aria-label="Card front">
    <h1 class="front-name">Ned Halvorsen</h1>
    <p class="front-tagline">Clinical Psychotherapist and Executive Coach<br>For Personal and Professional Success</p>
  </section>

  <section class="card card-back" aria-label="Card back">
    <div class="addresses">
      <p class="address">
        <svg class="icon" viewBox="0 0 12 12"><path d="M6 0a4 4 0 0 0-4 4c0 3 4 8 4 8s4-5 4-8a4 4 0 0 0-4-4zm0 5.6A1.6 1.6 0 1 1 6 2.4a1.6 1.6 0 0 1 0 3.2z"/></svg>
        <span>87 Tarrant Vale Road Tarrant<br>North Sydney</span>
      </p>
      <p class="address">
        <svg class="icon" viewBox="0 0 12 12"><path d="M6 0a4 4 0 0 0-4 4c0 3 4 8 4 8s4-5 4-8a4 4 0 0 0-4-4zm0 5.6A1.6 1.6 0 1 1 6 2.4a1.6 1.6 0 0 1 0 3.2z"/></svg>
        <span>Suite 512 / 248 Danforth Street<br>Sydney CBD</span>
      </p>
      <p class="address">
        <svg class="icon" viewBox="0 0 12 12"><path d="M6 0a4 4 0 0 0-4 4c0 3 4 8 4 8s4-5 4-8a4 4 0 0 0-4-4zm0 5.6A1.6 1.6 0 1 1 6 2.4a1.6 1.6 0 0 1 0 3.2z"/></svg>
        <span>Suite 309 / 41 Pellow Street North<br>Sydney Danforth Street</span>
      </p>
    </div>

    <div class="divider"></div>

    <div class="contact">
      <h2 class="contact-name">Ned Halvorsen</h2>
      <ul class="contact-list">
        <li>
          <svg class="icon" viewBox="0 0 12 12"><circle cx="6" cy="6" r="5.3" fill="none" stroke="#1d1d1d" stroke-width="1"/><path d="M4 3.2l1 1.3-.6.8a4 4 0 0 0 2.3 2.3l.8-.6 1.3 1-.7 1A5 5 0 0 1 3 4z"/></svg>
          <span>02 95517384</span>
        </li>
        <li>
          <svg class="icon" viewBox="0 0 12 12"><path d="M1 3h10v7H1z"/><path d="M1 3l5 4 5-4" fill="none" stroke="#fff" stroke-width="1"/></svg>
          <span>ned@nedhalvorsen.example.au</span>
        </li>
        <li>
          <svg class="icon" viewBox="0 0 12 12"><g fill="none" stroke="#1d1d1d" stroke-width="1"><circle cx="6" cy="6" r="5"/><ellipse cx="6" cy="6" rx="2.2" ry="5"/><path d="M1 6h10M2 3.5h8M2 8.5h8"/></g></svg>
          <span>www.nedhalvorsen.example.au</span>
        </li>
      </ul>
    </div>

    <svg class="bands" viewBox="0 0 540 60" aria-hidden="true">
      <polygon points="0,48 248,48 236,60 0,60" fill="var(--accent-black)"/>
      <polygon points="262,44 540,22 540,38 232,60" fill="var(--accent-red)"/>
      <polygon points="262,44 270,44 244,60 236,60" fill="#ffffff"/>
    </svg>
  </section>
</main>
</body>
</html>
```